Meadowlark Hearing and Tinnitus Solutions - Let's help people flourish with better hearing!

I am a private practice audiologist that focuses on hearing and tinnitus treatment. My job allows me the opportunity to help people to improve their lives with better communication, connecting them with family, friends, the people that matter the most. I love what I do. The design should communicate warmth and professionalism. A modern approach to an affliction that effects people of all ages. A like a natural color pallet with turquoise as an accent. I just want something powerful that will motivate people to make an appointment.

Industry/Entity Type

Communication

```html
<!DOCTYPE html>
<html lang="en">
<head>
<meta charset="utf-8">
<title>Meadowlark Hearing and Tinnitus Solutions</title>
<link rel="stylesheet" href="https://fonts.googleapis.com/css2?family=Questrial&display=swap">
<style>
  :root {
    --page: #ffffff;
    --ink: #121412;
    --teal-deep: #13a592;
    --teal: #1cc1a6;
    --teal-light: #3fd6c4;
  }
  html, body {
    margin: 0;
    padding: 0;
    width: 1200px;
    height: 1000px;
    overflow: hidden;
    background: var(--page);
  }
  .canvas {
    position: relative;
    width: 1200px;
    height: 1000px;
  }
  .banner {
    position: absolute;
    left: 188px;
    top: 348px;
    width: 825px;
    height: 305px;
    overflow: hidden;
  }
  .banner-backdrop {
    position: absolute;
    inset: 0;
    background: linear-gradient(180deg, var(--teal) 0%, var(--teal-light) 50%, var(--teal-deep) 100%);
  }
  .lockup {
    position: absolute;
    left: 267px;
    top: 40px;
    width: 285px;
    text-align: center;
    color: var(--ink);
    font-family: "Questrial", sans-serif;
  }
  .lockup-name {
    margin: 0;
    height: 128px;
    line-height: 160px;
    font-size: 50px;
    font-weight: 400;
    letter-spacing: 0.5px;
    white-space: nowrap;
  }
  .lockup-rule {
    height: 1.5px;
    background: var(--ink);
  }
  .lockup-services {
    margin: 0;
    padding: 3px 0 5px;
    font-size: 25px;
    line-height: 32px;
    font-weight: 400;
    letter-spacing: 0.2px;
    white-space: nowrap;
  }
</style>
</head>
<body>
  <main class="canvas">
    <section class="banner">
      <div class="banner-backdrop" role="img" aria-label="Turquoise background artwork of light rays bursting from the centre"></div>
      <div class="lockup">
        <h1 class="lockup-name">Meadowlark</h1>
        <div class="lockup-rule"></div>
        <p class="lockup-services">HEARING &amp; TINNITUS<br>SOLUTIONS</p>
        <div class="lockup-rule"></div>
      </div>
    </section>
  </main>
</body>
</html>
```